mothers day ad for martial arts school

I am looking to have a nice flyer/handout to promote my martial arts school. It is for our promotion of "mom's train free" for mothers day in May. I would like an ad that would inspire a mother to learn self defense and to improve their fitness. It can have pictures but not necessarily a requirement. Pictures don't have to be of a lady in a martial arts uniform. It may be better if they are not. It also doesn't have to be standard sheet of paper size, as these are going to be handouts the size can be smaller. I would like our Crane Hollow logo on the flyer.

Target Market(s)

mothers that hadn't thought about martial arts before but would be convinced to try it

Industry/Entity Type

School

Requirements
Must have
• text, photos that would appeal to and encourage a mother to try a self defense/fitness class
Nice to have
• our logo and text and possibly pictures that would inspire a mother to join a martial arts class

```html
<!DOCTYPE html>
<html lang="en">
<head>
<meta charset="utf-8">
<title>Mothers Train Free – Crane Hollow Martial Arts</title>
<link href="https://fonts.googleapis.com/css2?family=Questrial&family=Anton&display=swap" rel="stylesheet">
<style>
  :root {
    --sky-light: #a9ddf6;
    --sky-mid: #72c3ee;
    --sky-deep: #4ea9e2;
    --shirt-dark: #2b3440;
    --skin-warm: #d9b2a0;
    --band-blue: #6ba4d9;
    --promo-red: #d42030;
    --ink: #111111;
    --paper: #ffffff;
  }
  html, body {
    margin: 0;
    padding: 0;
    width: 850px;
    height: 1200px;
    overflow: hidden;
    background: var(--paper);
  }
  .flyer {
    position: relative;
    width: 850px;
    height: 1200px;
    overflow: hidden;
    background: var(--paper);
    font-family: "Questrial", sans-serif;
    color: var(--ink);
  }
  .hero-photo {
    position: absolute;
    left: 0;
    top: 0;
    width: 850px;
    height: 620px;
    background:
      radial-gradient(ellipse 420px 300px at 330px 420px, rgba(43, 52, 64, 0.75) 0%, rgba(43, 52, 64, 0) 100%),
      radial-gradient(ellipse 380px 240px at 520px 260px, rgba(217, 178, 160, 0.55) 0%, rgba(217, 178, 160, 0) 100%),
      linear-gradient(160deg, var(--sky-light) 0%, var(--sky-mid) 55%, var(--sky-deep) 100%);
  }
  .swooshes {
    position: absolute;
    left: 0;
    top: 0;
  }
  .brand-top {
    position: absolute;
    top: 32px;
    right: 28px;
    display: flex;
    align-items: center;
    gap: 10px;
    font-size: 30px;
    letter-spacing: 1px;
    color: var(--ink);
  }
  .brand-top .mark {
    width: 26px;
    height: 26px;
    background: var(--promo-red);
  }
  .promo-headline {
    position: absolute;
    left: 192px;
    top: 616px;
    margin: 0;
    font-weight: 400;
    font-size: 36px;
    line-height: 50px;
    color: var(--paper);
    white-space: nowrap;
  }
  .call-to-action {
    position: absolute;
    left: 46px;
    top: 893px;
    margin: 0;
    font-family: "Anton", sans-serif;
    font-weight: 400;
    font-size: 32px;
    line-height: 35px;
    letter-spacing: 1.6px;
    color: var(--ink);
  }
  .call-to-action .accent {
    display: block;
    color: var(--promo-red);
  }
  .benefits {
    position: absolute;
    left: 46px;
    top: 984px;
    margin: 0;
    padding: 0;
    list-style: none;
    font-size: 30px;
    line-height: 38px;
    color: var(--ink);
  }
  .brand-bottom {
    position: absolute;
    right: 26px;
    top: 1086px;
    text-align: center;
    color: var(--promo-red);
    font-size: 12px;
    letter-spacing: 4px;
    line-height: 1;
  }
  .brand-bottom .name-large {
    display: block;
    font-size: 46px;
    letter-spacing: 2px;
    margin: 6px 0 6px;
  }
</style>
</head>
<body>
  <main class="flyer">
    <div class="hero-photo" role="img" aria-label="Photo of two women in black training shirts holding their fists up in a fighting stance against a light blue backdrop"></div>

    <svg class="swooshes" width="850" height="1200" viewBox="0 0 850 1200" aria-hidden="true">
      <path class="photo-corner" d="M0,404 C90,500 190,560 300,588 L0,594 Z" fill="var(--band-blue)"/>
      <path class="paper-cover" d="M0,592 C300,606 650,496 850,290 L850,1200 L0,1200 Z" fill="var(--paper)"/>
      <path class="red-swoosh" d="M0,600 C300,614 650,504 850,302 L850,842 C560,842 320,800 160,730 C90,700 40,650 0,615 Z" fill="var(--promo-red)"/>
      <path class="blue-band" d="M160,738 C330,830 560,890 850,952 L850,858 C560,856 330,820 160,738 Z" fill="var(--band-blue)"/>
    </svg>

    <div class="brand-top">
      <span class="mark"></span>
      <span class="name">CRANE HOLLOW</span>
    </div>

    <h1 class="promo-headline">MOTHERS TRAIN FREE FOR 30 DAYS<br>WHEN YOU START BY MAY 31ST!</h1>

    <h2 class="call-to-action">MOTHERS, COME GET<span class="accent">TRAINED TODAY!</span></h2>

    <ul class="benefits">
      <li>FEEL STRONG</li>
      <li>LOOK GOOD</li>
      <li>GET STRONG</li>
      <li>FEEL SAFE</li>
    </ul>

    <div class="brand-bottom">
      <span>CRANE HOLLOW</span>
      <span class="name-large">ASCEND</span>
      <span>MARTIAL ARTS</span>
    </div>
  </main>
</body>
</html>
```